"sweetpailo!" hand crafted, premium gelato needs a delicious design!

SweetPailo!
Hand Crafted, Premium, Delicious (tag line to be included)

We are artisan gelato craftsmen, passionate about the art of making gelato. Our philosophy to crafting our premium gelato is pure and simple.
Always use quality fresh ingredients
Keep learning, always improving and honing our gelato crafting skills
We believe that this simple philosophy is the key to our Delicious, Premium and Authentic gelato that is SweetPailo!

Where possible, we source our key ingredients from local producers who in their own right are proud and passionate about their produce.

The logo should be clean and communicate a premium, artisan, hand crafted product.

I will require a front label which describes the flavor of the gelato and a rear ingredients/nutritional facts label.

The rear label needs to be easily modifiable according to the flavor and ingredients used, as we add to our flavor list.

There should also be a space to insert a nutrition label - I've uploaded an example of a nutrition label

As an example for rear label

___________________________________________________________________________
Our artisan Gelato is proudly hand crafted in small batches with love, passion and with local Australian produce whenever possible. We use Fresh Milk and Pure Cream sourced from local producers who are equally passionate about their produce.

We only use All Natural ingredients. Free from any artificial colours, flavours, and preservatives.

Ingredients
Fresh Milk, Pure Cream, Skim Milk Powder, Sugar, Dextrose, Japanese Matcha, Arrowroot Flour. Guar Gum

Contains Milk, Wheat

Although we do not use nuts, some of the ingredients we use may have been processed on equipment that may have processed nuts.

Best Stored Frozen at minus 18°C

We would love to hear from you!
www.sweetpailo.com.au
gelato@sweetpailo.com.au
(place facebook logo here)

Example of a label I like:

http://www.wrapmuseboard.example/tondo-artisan-gelato.html/

I would like to showcase the end product as much as possible so the label should be transparent and enhance the flavor of the gelato. A small graphic complimenting the key ingredient the flavor would be enhancing the product.

Some of the examples of the flavors we have are
Japanese Matcha * this will be the main flavour
Kestrel Hills Chocolate Bar
Dunmore Creek Salted Caramel
Vanilla Bean

Please note that there is future paid opportunity to make modifications to the front label and ingredients label as we keep adding flavors so I am looking for a designer that I can have a long term partnership with. Thanks! Added Wednesday, October 12, 2016

Target Market(s)

Retail space looking for a premium alternative to the high end ice cream. People who appreciate artisan products

Logo Text

SweetPailo!- Premium, Hand Crafted, Delicious

Requirements
Must have
• must highlight the key ingredient of each flavor

```html
<!DOCTYPE html>
<html lang="en">
<head>
<meta charset="utf-8">
<title>SweetPailo! Japanese Matcha – Front Label</title>
<link href="https://fonts.googleapis.com/css2?family=Oswald:wght@500;600&family=Pinyon+Script&family=Mrs+Saint+Delafield&display=swap" rel="stylesheet">
<style>
  :root {
    --matcha-base: #8ddf7f;
    --matcha-light: #9fe892;
    --matcha-deep: #63cc5a;
    --label-ink: #0f7a22;
    --label-white: #ffffff;
    --leaf-tone: #e9f7e4;
  }
  html, body {
    margin: 0;
    padding: 0;
    width: 1200px;
    height: 1200px;
    overflow: hidden;
  }
  .label {
    position: relative;
    width: 1200px;
    height: 1200px;
    background: radial-gradient(ellipse at 50% 55%, var(--matcha-light) 0%, var(--matcha-base) 55%, var(--matcha-deep) 100%);
    font-family: "Oswald", sans-serif;
  }
  .label__sprig {
    position: absolute;
    left: 540px;
    top: 60px;
    width: 150px;
    height: 150px;
  }
  .label__flavour-origin {
    position: absolute;
    left: 0;
    right: 0;
    top: 240px;
    margin: 0;
    text-align: center;
    font-family: "Pinyon Script", cursive;
    font-weight: 400;
    font-size: 190px;
    line-height: 1;
    color: var(--label-white);
    letter-spacing: -2px;
  }
  .label__flavour {
    position: absolute;
    left: 0;
    right: 0;
    top: 420px;
    margin: 0;
    text-align: center;
    font-family: "Oswald", sans-serif;
    font-weight: 600;
    font-size: 230px;
    line-height: 1;
    color: var(--label-ink);
    transform: scaleX(0.82);
    letter-spacing: -2px;
  }
  .label__divider {
    position: absolute;
    left: 330px;
    top: 690px;
    width: 540px;
    height: 50px;
  }
  .label__brand {
    position: absolute;
    left: 0;
    right: 0;
    top: 765px;
    margin: 0;
    text-align: center;
    font-family: "Oswald", sans-serif;
    font-weight: 600;
    font-size: 84px;
    line-height: 1;
    color: var(--label-ink);
    transform: scaleX(0.82);
  }
  .label__tagline {
    position: absolute;
    left: 0;
    right: 0;
    top: 885px;
    margin: 0;
    text-align: center;
    font-family: "Mrs Saint Delafield", cursive;
    font-size: 62px;
    line-height: 48px;
    color: var(--label-white);
  }
  .label__tagline span { display: block; }
</style>
</head>
<body>
  <main class="label">
    <svg class="label__sprig" role="img" aria-label="Line illustration of a green tea leaf sprig" viewBox="0 0 150 150">
      <rect width="150" height="150" rx="18" fill="var(--leaf-tone)" opacity="0.55"/>
    </svg>

    <h2 class="label__flavour-origin">Japanese</h2>
    <h1 class="label__flavour">MATCHA</h1>

    <svg class="label__divider" role="img" aria-label="Decorative flourish divider with swirls" viewBox="0 0 540 50">
      <rect width="540" height="50" rx="25" fill="var(--leaf-tone)" opacity="0.45"/>
    </svg>

    <p class="label__brand">SweetPailo!</p>

    <p class="label__tagline">
      <span>Hand crafted</span>
      <span>Premium</span>
      <span>Delicious</span>
    </p>
  </main>
</body>
</html>
```